BrightHarbor Flowchart Marketing Flyer

We are an MSP IT company. We have created a flowchart that we would like jazzed up to use in marketing new customers. The flowchart is a visual for prospective clients to see, in a simple way, what our process is. The flowchart should be 8.5"x11". We do not want the template of the flowchart altered (no boxes moved around) but would like something visually appealing and clean looking. Our office colors are lime green, royal blue, with accent colors of orange and purple. We would like the colors incorporated into the design. The design should be modern. This flyer is not going to be mass mailed. It will be handed to a prospective client in a face to face meeting.
Updates

I have uploaded our company logo to my brief in a couple of formats. One of the designers requested this. Great idea! I apologize for not providing it to begin with - it's my first time using this Website and the first time I have been assigned a project.

I was not able to view over the weekend as I did not have access to my work computer. Also need to review with the rest of management team on Thursday 6/28

Target Market(s)

Potential clients for an MSP IT company

Industry/Entity Type

It Company

Requirements
Must have
• The template itself we don't want changed. In other words we don't want the boxes moved around.
Nice to have
• Text, lines, shading and color of boxes can be changed. Not all colors mentioned in the brief need to be used. Would like it easy on the eye.

```html
<!DOCTYPE html>
<html lang="en">
<head>
<meta charset="utf-8">
<title>BrightHarbor Process Flyer</title>
<link rel="stylesheet" href="https://fonts.googleapis.com/css2?family=Barlow:wght@600;700&family=Barlow+Semi+Condensed:wght@600;700&family=Montserrat:wght@500&display=swap">
<style>
  :root {
    --backdrop: #e4e6e9;
    --paper: #ffffff;
    --ink: #231f20;
    --royal-blue: #0f5ca8;
    --lime-light: #a6ce39;
    --lime-dark: #7abf43;
    --purple: #92278f;
    --orange-deep: #e8632a;
    --orange-light: #f7941d;
    --orange-fold: #b4441a;
    --rail: #c4c4c4;
    --pill-text: #333333;
  }
  html, body {
    margin: 0;
    width: 1200px;
    height: 1200px;
    overflow: hidden;
    background: var(--backdrop);
  }
  .flyer {
    position: absolute;
    left: 0;
    top: 136px;
    width: 1200px;
    height: 927px;
    display: block;
  }
  .title { font-family: "Barlow", sans-serif; font-weight: 700; font-size: 50px; fill: var(--ink); letter-spacing: 0.5px; }
  .brand-name { font-family: "Barlow", sans-serif; font-weight: 700; font-size: 28px; fill: var(--royal-blue); }
  .step-label { font-family: "Montserrat", sans-serif; font-weight: 500; font-size: 17px; fill: #ffffff; text-anchor: middle; }
  .bullet { font-family: "Barlow Semi Condensed", sans-serif; font-weight: 700; font-size: 11.5px; fill: var(--ink); }
  .banner-text { font-family: "Barlow Semi Condensed", sans-serif; font-weight: 700; font-size: 18px; fill: #ffffff; }
  .pill-text { font-family: "Montserrat", sans-serif; font-weight: 500; font-size: 13px; fill: var(--pill-text); text-anchor: middle; }
  .rail { stroke: var(--rail); stroke-width: 3; fill: none; }
  .cycle-arc { stroke: #ffffff; stroke-width: 2.5; fill: none; }
</style>
</head>
<body>
<svg class="flyer" viewBox="199 289 1102 851" xmlns="http://www.w3.org/2000/svg">
  <defs>
    <linearGradient id="lime" x1="0" y1="0" x2="1" y2="0">
      <stop offset="0" stop-color="var(--lime-light)"/>
      <stop offset="1" stop-color="var(--lime-dark)"/>
    </linearGradient>
    <linearGradient id="orange" x1="0" y1="0" x2="1" y2="0">
      <stop offset="0" stop-color="var(--orange-deep)"/>
      <stop offset="1" stop-color="var(--orange-light)"/>
    </linearGradient>
    <filter id="pill-shadow" x="-20%" y="-20%" width="140%" height="160%">
      <feDropShadow dx="0" dy="2" stdDeviation="1.5" flood-opacity="0.3"/>
    </filter>
  </defs>

  <rect class="sheet" x="199" y="289" width="1102" height="851" fill="var(--paper)"/>

  <!-- header -->
  <text class="title" x="235" y="382">BRIGHTHARBOR PROCESS</text>
  <g class="brand">
    <circle cx="1085" cy="361" r="12" fill="var(--royal-blue)"/>
    <text class="brand-name" x="1105" y="371">BrightHarbor</text>
  </g>
  <rect class="header-rule" x="235" y="411" width="1030" height="10" fill="var(--royal-blue)"/>

  <!-- timeline -->
  <g class="timeline">
    <circle cx="250" cy="591" r="7" fill="var(--rail)"/>
    <line class="rail" x1="250" y1="591" x2="884" y2="591"/>
    <polygon points="880,575 908,591 880,607" fill="var(--rail)"/>
    <g class="milestone">
      <circle cx="348" cy="591" r="26" fill="#fff" stroke="var(--rail)" stroke-width="3"/>
      <circle cx="348" cy="591" r="14" fill="url(#lime)"/>
      <line class="rail" x1="348" y1="617" x2="348" y2="638"/>
    </g>
    <g class="milestone">
      <circle cx="565" cy="591" r="26" fill="#fff" stroke="var(--rail)" stroke-width="3"/>
      <circle cx="565" cy="591" r="14" fill="url(#lime)"/>
      <line class="rail" x1="565" y1="617" x2="565" y2="638"/>
    </g>
    <g class="milestone">
      <circle cx="782" cy="591" r="26" fill="#fff" stroke="var(--rail)" stroke-width="3"/>
      <circle cx="782" cy="591" r="14" fill="url(#lime)"/>
      <line class="rail" x1="782" y1="617" x2="782" y2="638"/>
    </g>
  </g>

  <!-- step boxes -->
  <g class="step">
    <rect x="260" y="638" width="177" height="91" fill="url(#lime)"/>
    <text class="step-label" x="345" y="679">ASSESS</text>
    <text class="step-label" x="345" y="702">ALIGNMENT</text>
    <polygon points="447,675 456,683 447,691" fill="var(--rail)"/>
    <path class="rail" d="M348 729 V793 H259 V865"/>
    <text class="bullet" x="271" y="821">• REVIEW TECHNOLOGY PHILOSOPHY</text>
    <text class="bullet" x="271" y="842">• SHARE PROPRIETARY METHOD</text>
    <text class="bullet" x="271" y="863">• ASSESS ORGANIZATIONAL FIT</text>
  </g>
  <g class="step">
    <rect x="477" y="638" width="177" height="91" fill="url(#lime)"/>
    <text class="step-label" x="564" y="691">ON BOARDING</text>
    <polygon points="665,675 674,683 665,691" fill="var(--rail)"/>
    <path class="rail" d="M565 729 V793 H476 V886"/>
    <text class="bullet" x="488" y="821">• ESTABLISH EXPECTATIONS</text>
    <text class="bullet" x="488" y="842">• SERVICE PROVIDER TRANSITION</text>
    <text class="bullet" x="490" y="863">• CYBERSECURITY REVIEW</text>
    <text class="bullet" x="488" y="884">• BACKUP/PROTECTION STRATEGY</text>
  </g>
  <g class="step">
    <rect x="694" y="638" width="177" height="91" fill="url(#lime)"/>
    <text class="step-label" x="782" y="679">30 DAY</text>
    <text class="step-label" x="782" y="702">EVALUATION</text>
    <polygon points="882,675 891,683 882,691" fill="var(--rail)"/>
    <path class="rail" d="M782 729 V793 H693 V886"/>
    <text class="bullet" x="708" y="821">• DEVELOP IT PLAYBOOK</text>
    <text class="bullet" x="708" y="842">• MAJOR RISK IDENTIFICATION</text>
    <text class="bullet" x="708" y="863">• OBSERVE &amp; DOCUMENT TRENDS</text>
    <text class="bullet" x="708" y="884">• STANDARDS ALIGNMENT PLAN•</text>
  </g>

  <!-- ongoing cycle panel -->
  <g class="cycle-panel">
    <rect x="928" y="456" width="330" height="386" fill="var(--purple)"/>
    <polygon points="909,538 928,538 928,552" fill="var(--orange-fold)"/>
    <rect x="909" y="487" width="335" height="51" fill="url(#orange)"/>
    <text class="banner-text" x="936" y="517">Ongoing Strategic Plan &amp; Execution</text>

    <path class="cycle-arc" d="M980 637 A38 38 0 0 1 1018 599"/>
    <path class="cycle-arc" d="M1175 599 A38 38 0 0 1 1213 637"/>
    <path class="cycle-arc" d="M980 741 A38 38 0 0 0 1018 779"/>
    <path class="cycle-arc" d="M1213 741 A38 38 0 0 1 1175 779"/>

    <g filter="url(#pill-shadow)" fill="#ffffff">
      <rect x="1043" y="579" width="107" height="39" rx="5"/>
      <rect x="945" y="665" width="106" height="39" rx="5"/>
      <rect x="1135" y="668" width="107" height="39" rx="5"/>
      <rect x="1040" y="757" width="107" height="38" rx="5"/>
    </g>
    <text class="pill-text" x="1096" y="604">STRATEGY</text>
    <text class="pill-text" x="998" y="682">RISK</text>
    <text class="pill-text" x="998" y="697">ASSESSMENT</text>
    <text class="pill-text" x="1188" y="684">STANDARDS</text>
    <text class="pill-text" x="1188" y="699">ALIGNMENT</text>
    <text class="pill-text" x="1093" y="781">BUDGET</text>
  </g>

  <g class="ongoing-notes">
    <path class="rail" d="M1093 842 V904 H929 V1019"/>
    <text class="bullet" x="944" y="933">• DEVELOP &amp; EXECUTE ANNUAL STRATEGIC PLAN</text>
    <text class="bullet" x="944" y="954">• RISK ASSESSMENT, RANKING, MITIGATION</text>
    <text class="bullet" x="944" y="975">• PRIORITIZE INVESTMENTS</text>
    <text class="bullet" x="944" y="996">• DEVELOP 5 YEAR BUDGET</text>
    <text class="bullet" x="944" y="1017">• HARBORPLAN™ STANDARD ALIGNMENT</text>
  </g>

  <rect class="footer-band" x="199" y="1074" width="1102" height="66" fill="var(--royal-blue)"/>
</svg>
</body>
</html>
```